Corvane Electronics, Inc. Business card

Incorporate a globe.
We repair electronics, sell electronic parts, and we recycle electronics. We've been in business since 1982. A technology feel to the card is preferred. I want to be able to give this card to a client from different industries and make it relate-able. I don't have a logo that I've been partial to in the past. It is not necessary in this case.

Target Market(s)

Consumer, Industrial, Business, Medical

Industry/Entity Type

Business

Contact Information for Business Card

4518 Maple Crest Blvd. Dallas, TX 75207
214-555-0187 main 214-555-0143 fax
Paul Bredesen VP

Font styles to use
Serif

Requirements
Must have
• Technology feel
Nice to have
• Metallic look
Should not have
• no pastel colors

```html
<!DOCTYPE html>
<html lang="en">
<head>
<meta charset="utf-8">
<title>Corvane Electronics, Inc. – Business Card</title>
<link href="https://fonts.googleapis.com/css2?family=Open+Sans:wght@400;600&display=swap" rel="stylesheet">
<style>
  :root {
    --backdrop: #e4e5e7;
    --card: #ffffff;
    --brand-blue: #1f8ac6;
    --blue-light: #2aa6e0;
    --ink: #2b2b2b;
    --steel: #5b5c5e;
    --steel-light: #a9aaac;
    --rule: #cfd0d2;
    --ghost: #f3f3f4;
  }
  * { box-sizing: border-box; margin: 0; padding: 0; }
  html, body {
    width: 1200px; height: 1000px; overflow: hidden;
    background: var(--backdrop);
    font-family: "Open Sans", Arial, sans-serif;
  }
  .card {
    position: absolute; left: 265px; width: 665px; height: 397px;
    background: var(--card); overflow: hidden;
  }
  .card-front { top: 73px; }
  .card-back { top: 532px; }

  .ghost-globe {
    position: absolute; left: 50px; top: 30px;
    width: 330px; height: 330px; border-radius: 50%;
    background: var(--ghost);
  }

  .brand { position: absolute; display: flex; align-items: center; }
  .brand-mark { border-radius: 50%; background: var(--brand-blue); flex: none; }
  .brand-name {
    color: var(--steel); font-weight: 600; text-transform: uppercase; line-height: 1.05;
  }
  .brand-name span { display: block; }

  .card-front .brand { left: 293px; top: 63px; }
  .card-front .brand-mark { width: 84px; height: 84px; margin-right: 14px; }
  .card-front .brand-name .first { font-size: 40px; letter-spacing: 2px; }
  .card-front .brand-name .second { font-size: 22px; letter-spacing: 1.5px; }

  .card-back .brand { left: 120px; top: 136px; }
  .card-back .brand-mark { width: 132px; height: 132px; margin-right: 20px; }
  .card-back .brand-name .first { font-size: 58px; letter-spacing: 3px; }
  .card-back .brand-name .second { font-size: 32px; letter-spacing: 2px; }

  .person { position: absolute; left: 33px; top: 206px; }
  .person-name { color: var(--brand-blue); font-size: 21px; font-weight: 600; line-height: 1.2; }
  .person-title { color: var(--ink); font-size: 16px; line-height: 1.3; }

  .divider {
    position: absolute; left: 33px; top: 267px; width: 452px; height: 1px;
    background: var(--rule);
  }

  .address {
    position: absolute; left: 33px; top: 292px;
    color: var(--ink); font-size: 16px; font-style: normal; line-height: 24px;
  }

  .contacts {
    position: absolute; right: 30px; top: 255px; list-style: none;
    color: var(--ink); font-size: 16px; line-height: 24.5px; text-align: right;
  }
  .contacts li { display: flex; justify-content: flex-end; align-items: center; }
  .contacts svg { width: 16px; height: 16px; margin-left: 7px; fill: var(--brand-blue); }

  .footer-bands { position: absolute; left: 0; bottom: 0; width: 665px; height: 28px; }
</style>
</head>
<body>

<section class="card card-front" aria-label="Business card front">
  <div class="ghost-globe" aria-hidden="true"></div>

  <div class="brand">
    <div class="brand-mark"></div>
    <div class="brand-name"><span class="first">Corvane</span><span class="second">Electronics</span></div>
  </div>

  <div class="person">
    <p class="person-name">PAUL BREDESEN</p>
    <p class="person-title">Vice President</p>
  </div>

  <div class="divider"></div>

  <address class="address">4518 Maple Crest Blvd.<br>Dallas, TX 75207</address>

  <ul class="contacts">
    <li>+ 000 000 0000
      <svg viewBox="0 0 16 16" aria-hidden="true"><path d="M4 1h8v14H4z M5 3v7h6V3z" fill-rule="evenodd"/></svg>
    </li>
    <li>+ 000 000 0000
      <svg viewBox="0 0 16 16" aria-hidden="true"><path d="M1 6c2-3 12-3 14 0l-1 2-3-1V5H5v2L2 8z M3 9h10l1 5H2z"/></svg>
    </li>
    <li>info@corvaneelectronics.com
      <svg viewBox="0 0 16 16" aria-hidden="true"><path d="M1 3h14v10H1z M2 4l6 5 6-5z" fill-rule="evenodd"/></svg>
    </li>
    <li>www.corvaneelectronics.com
      <svg viewBox="0 0 16 16" aria-hidden="true"><path d="M8 1a7 7 0 1 0 0 14A7 7 0 0 0 8 1z M3 7h10v2H3z M7 2h2v12H7z" fill-rule="evenodd"/></svg>
    </li>
  </ul>

  <svg class="footer-bands" viewBox="0 0 665 28" aria-hidden="true">
    <defs>
      <linearGradient id="band-blue" x1="0" x2="1">
        <stop offset="0" stop-color="#1f7fb8"/>
        <stop offset="1" stop-color="#2aa8e2"/>
      </linearGradient>
      <linearGradient id="band-steel" x1="0" x2="1">
        <stop offset="0" stop-color="#b4b5b7"/>
        <stop offset="1" stop-color="#58595b"/>
      </linearGradient>
    </defs>
    <polygon points="0,11 337,11 318,28 0,28" fill="url(#band-blue)"/>
    <polygon points="350,0 665,0 665,28 323,28" fill="url(#band-steel)"/>
  </svg>
</section>

<section class="card card-back" aria-label="Business card back">
  <div class="brand">
    <div class="brand-mark"></div>
    <div class="brand-name"><span class="first">Corvane</span><span class="second">Electronics</span></div>
  </div>
</section>

</body>
</html>
```